RTB sticker for the back window of a car

Well this design is for the back of our car. We want it to be plain and simple but stand out. I have put something together which is a bit to plain and i would like to to look a little bit different. Possibly have a picture of a shipping container on it so people know what we are trying to sell? I don't need our logo on there but i want the phone number and email. Thank you in advance.

Requirements
Must have
• The phone number 0452 317 906 not the one in the picture please.
• Also must have the email that IS in the picture please.
Nice to have
• A picture of a shipping container so people know what we are talking about.

```html
<!DOCTYPE html>
<html lang="en">
<head>
<meta charset="utf-8">
<title>RTB Shipping Containers – Rear Window Sticker</title>
<link rel="stylesheet" href="https://fonts.googleapis.com/css2?family=Archivo+Black&display=swap">
<style>
  :root {
    --page-bg: #e9e9ea;
    --sky-top: #f4f5f6;
    --sky-bottom: #c9ccd0;
    --container-red-light: #a5242d;
    --container-red: #7d1119;
    --container-red-dark: #4a070c;
    --interior: #0b0b0b;
    --ink: #111111;
    --white: #ffffff;
    --accent-red: #e0262f;
  }
  * { margin: 0; padding: 0; box-sizing: border-box; }
  html, body { width: 1200px; height: 930px; overflow: hidden; }
  body { background: var(--page-bg); position: relative; font-family: "Archivo Black", "Arial Black", sans-serif; }

  .window-sticker {
    position: absolute; left: 40px; top: 265px;
    width: 1120px; height: 400px;
    border-radius: 28px 28px 14px 14px;
    overflow: hidden;
    background: linear-gradient(var(--sky-top), var(--sky-bottom) 40%, var(--sky-bottom));
  }
  .container-artwork {
    position: absolute; left: 0; right: 0; top: 92px; bottom: 0;
    background: linear-gradient(90deg, var(--container-red-dark), var(--container-red) 20%, var(--container-red-light) 45%, var(--container-red-light) 55%, var(--container-red) 80%, var(--container-red-dark));
  }
  .container-interior {
    position: absolute; left: 368px; top: 100px;
    width: 384px; height: 270px;
    background: var(--interior);
  }
  .headline {
    position: absolute; left: 0; right: 0; top: 18px;
    text-align: center; color: var(--ink);
    font-size: 37px; line-height: 0.98; letter-spacing: 1px;
  }
  .offer {
    position: absolute; left: 368px; top: 120px; width: 384px;
    text-align: center; color: var(--white);
    font-size: 72px; line-height: 0.98; letter-spacing: 2px;
  }
  .contact {
    position: absolute; left: 368px; top: 278px; width: 384px;
    list-style: none; color: var(--white);
  }
  .contact-item { display: flex; align-items: center; justify-content: center; gap: 8px; }
  .contact-phone { font-size: 31px; letter-spacing: 1px; }
  .contact-email { font-size: 22px; margin-top: 6px; }
  .contact-icon { flex: none; }
</style>
</head>
<body>
  <section class="window-sticker">
    <div class="container-artwork" role="img" aria-label="Red shipping container with both doors swung open"></div>
    <div class="container-interior"></div>
    <h1 class="headline">SHIPPING<br>CONTAINERS</h1>
    <p class="offer">FOR<br>SALE</p>
    <ul class="contact">
      <li class="contact-item contact-phone">
        <svg class="contact-icon" width="26" height="26" viewBox="0 0 24 24" aria-hidden="true">
          <circle cx="12" cy="12" r="12" fill="var(--accent-red)"/>
          <path d="M8.2 5.5l2 2.6-1.2 1.5c.8 1.9 2.3 3.4 4.2 4.3l1.5-1.2 2.6 2-1.3 2.2c-4.8-.6-9-4.8-9.6-9.6z" fill="#fff"/>
        </svg>
        <span>0452 317 906</span>
      </li>
      <li class="contact-item contact-email">
        <svg class="contact-icon" width="22" height="22" viewBox="0 0 24 24" aria-hidden="true">
          <rect x="2" y="5" width="20" height="14" rx="3" fill="none" stroke="var(--accent-red)" stroke-width="2.4"/>
          <path d="M3 7l9 6 9-6" fill="none" stroke="var(--accent-red)" stroke-width="2.4"/>
        </svg>
        <span>sales@rtbcm.com.au</span>
      </li>
    </ul>
  </section>
</body>
</html>
```